Tattoo Shop Business Card

I need a Business Card for the The Harbor Quill.

I'm thinking i want a double sided business card, really clean, very classy, one side the logo, and on the other my information. I'm pretty much open to anything, as long as its fun and captures class and elegance, while at the same time is edgy and tattooish.
I don't want your typical classic card. Add your own twist on it

Logo is attached to this brief

Please include:
Name
Position
Phone Number
Email
Website

Target Market(s)

I'm looking to capture potential clients for my tattoo shop so the card needs to be something they can fit in their wallet but they will also remember me when they see that card in there. My target audience is everyone over 18 that is intrigued by tattoos and piercings.

Industry/Entity Type

Business

Font styles to use
Serif

Colors

Designer to choose colors to be used in the design.

Requirements
Must have
• must be bold and something people will never forget

```html
<!DOCTYPE html>
<html lang="en">
<head>
<meta charset="utf-8">
<title>The Harbor Quill – Business Card</title>
<link rel="stylesheet" href="https://fonts.googleapis.com/css2?family=Arimo:wght@400;700&display=swap">
<style>
  :root {
    --stage: #ebebeb;
    --card-white: #ffffff;
    --card-edge: #8f8f8f;
    --pink-light: #eba6b6;
    --pink-mid: #e891a6;
    --pink-deep: #e05a7e;
    --ink: #231f20;
    --accent: #e0284f;
  }
  * { margin: 0; padding: 0; box-sizing: border-box; }
  html, body {
    width: 1200px;
    height: 686px;
    overflow: hidden;
    background: var(--stage);
    font-family: "Arimo", Arial, sans-serif;
    color: var(--ink);
  }
  .stage { position: relative; width: 1200px; height: 686px; }

  .card {
    position: absolute;
    top: 191px;
    width: 545px;
    height: 303px;
    border: 1px solid var(--card-edge);
  }
  .card--front {
    left: 60px;
    background: linear-gradient(150deg, var(--pink-light) 0%, var(--pink-mid) 60%, var(--pink-deep) 100%);
    display: flex;
    align-items: center;
    justify-content: center;
  }
  .front-brand {
    font-weight: 700;
    font-size: 50px;
    letter-spacing: 0.5px;
    color: var(--ink);
    margin-top: -14px;
  }

  .card--back { left: 614px; background: var(--card-white); }
  .holder-name {
    position: absolute;
    right: 30px;
    top: 14px;
    font-weight: 700;
    font-size: 47px;
  }
  .back-brand {
    position: absolute;
    left: 62px;
    top: 78px;
    font-weight: 700;
    font-size: 23px;
  }
  .contact-list { list-style: none; position: absolute; left: 29px; top: 140px; }
  .contact-item { display: flex; align-items: flex-start; font-size: 21px; line-height: 24px; margin-bottom: 9px; }
  .contact-item--address { font-size: 19px; line-height: 27px; margin-bottom: 2px; }
  .contact-icon {
    flex: none;
    width: 18px;
    height: 18px;
    margin: 4px 14px 0 0;
    background: var(--accent);
    display: flex;
    align-items: center;
    justify-content: center;
  }
  .contact-icon svg { width: 14px; height: 14px; }
</style>
</head>
<body>
<main class="stage">
  <section class="card card--front" aria-label="Card front">
    <span class="front-brand">The Harbor Quill</span>
  </section>

  <section class="card card--back" aria-label="Card back">
    <h1 class="holder-name">Marcus</h1>
    <p class="back-brand">The Harbor Quill</p>
    <ul class="contact-list">
      <li class="contact-item contact-item--address">
        <span class="contact-icon"><svg viewBox="0 0 14 14"><path d="M7 1.5 1 7h2v5h3V9h2v3h3V7h2z" fill="#fff"/></svg></span>
        <span>Tähtikuja 12 C<br>00810 Helsinki</span>
      </li>
      <li class="contact-item">
        <span class="contact-icon"><svg viewBox="0 0 14 14"><path d="M3.5 1.5 5.5 4 4.5 5.5c.8 1.7 2.2 3.1 4 4L10 8.5l2.5 2-1 2C6 12 2 8 1.5 2.5z" fill="#fff"/></svg></span>
        <span>040 5550192</span>
      </li>
      <li class="contact-item">
        <span class="contact-icon"><svg viewBox="0 0 14 14"><rect x="1.5" y="3.5" width="11" height="7" fill="none" stroke="#fff" stroke-width="1.2"/><path d="M1.5 3.5 7 8l5.5-4.5" fill="none" stroke="#fff" stroke-width="1.2"/></svg></span>
        <span>hello@harborquill.in</span>
      </li>
      <li class="contact-item">
        <span class="contact-icon"><svg viewBox="0 0 14 14" fill="none" stroke="#fff" stroke-width="1"><circle cx="7" cy="7" r="5.2"/><ellipse cx="7" cy="7" rx="2.3" ry="5.2"/><path d="M1.8 7h10.4M2.7 4.3h8.6M2.7 9.7h8.6"/></svg></span>
        <span>www.harborquill.in</span>
      </li>
    </ul>
  </section>
</main>
</body>
</html>
```